Birchline Septic Solutions

Would like to see some single sided ones but would also like to see some double sided with one sided only being the logo. Owners name is Tom Waldrick. Phone number is 555-214-8830
Services are pumping, inspections, installs, and repairs

Contact Information for Business Card

555-241-8830 Tom Waldrick Ashford Ridge, OH

```html
<!DOCTYPE html>
<html lang="en">
<head>
<meta charset="utf-8">
<title>Birchline Septic Solutions – Business Cards</title>
<link rel="stylesheet" href="https://fonts.googleapis.com/css2?family=Archivo+Black&family=Montserrat:wght@500;600;700&display=swap">
<style>
  :root {
    --backdrop: #4a484c;
    --card-white: #ffffff;
    --card-black: #141414;
    --ink: #111111;
    --ink-soft: #2a2a2a;
    --teal: #3cc4c0;
    --emboss: #3a3a3a;
    --text-light: #f2f2f2;
  }
  * { box-sizing: border-box; margin: 0; padding: 0; }
  html, body {
    width: 1200px; height: 876px; overflow: hidden;
    background: var(--backdrop);
    font-family: "Montserrat", sans-serif;
  }
  .sheet {
    width: 1200px; height: 876px;
    display: flex; align-items: center; justify-content: center; gap: 40px;
  }
  .card {
    position: relative;
    width: 540px; height: 309px;
    border-radius: 4px;
    overflow: hidden;
    box-shadow: 0 18px 40px rgba(0,0,0,.35);
  }

  /* Front */
  .card--front { background: var(--card-white); }
  .front__scene {
    position: absolute; left: 0; bottom: 0;
    width: 300px; height: 230px;
    background: linear-gradient(135deg, #ffffff 0%, #d9d9d9 35%, #3a3a3a 70%, #111111 100%);
    clip-path: polygon(0 18%, 55% 42%, 100% 40%, 100% 100%, 0 100%);
  }
  .front__brand {
    position: absolute; left: 30px; top: 30px;
    display: flex; align-items: center; gap: 10px;
  }
  .brand__mark { width: 14px; height: 14px; background: var(--teal); flex: none; }
  .brand__name {
    font-weight: 700; font-size: 17px; letter-spacing: .5px;
    color: var(--ink); width: 190px; line-height: 1.2;
    text-transform: uppercase;
  }
  .front__contact {
    position: absolute; right: 34px; top: 92px;
    text-align: right;
  }
  .contact__name {
    font-family: "Archivo Black", sans-serif;
    font-size: 24px; letter-spacing: 1.5px; color: var(--ink);
    text-transform: uppercase;
  }
  .contact__role {
    font-size: 15px; font-weight: 500; color: var(--teal);
    margin-top: 2px;
  }
  .contact__line {
    display: flex; align-items: center; justify-content: flex-end; gap: 8px;
    font-size: 15px; font-weight: 500; color: var(--ink-soft);
    letter-spacing: 1px; margin-top: 14px;
  }
  .contact__line + .contact__line { margin-top: 6px; }
  .contact__icon { width: 13px; height: 13px; fill: var(--teal); flex: none; }

  /* Back */
  .card--back { background: linear-gradient(120deg, #1b1b1b 0%, #0c0c0c 100%); }
  .back__brand {
    position: absolute; left: 0; right: 0; top: 86px;
    display: flex; align-items: center; justify-content: center; gap: 12px;
  }
  .back__brand .brand__mark { background: var(--teal); width: 16px; height: 16px; }
  .back__brand .brand__name {
    color: var(--emboss); font-size: 26px; width: auto; text-align: center;
  }
  .back__services {
    position: absolute; left: 0; right: 0; bottom: 30px;
    text-align: center;
    font-size: 14px; font-weight: 600; letter-spacing: 2.5px;
    color: var(--text-light); text-transform: uppercase;
  }
  .services__sep { color: var(--teal); margin: 0 6px; }
</style>
</head>
<body>
<main class="sheet">
  <section class="card card--front" aria-label="Business card front">
    <div class="front__scene" role="img" aria-label="Black silhouette illustration of pine trees and a rocky mountain peak"></div>
    <div class="front__brand">
      <span class="brand__mark"></span>
      <span class="brand__name">Birchline Septic Solutions</span>
    </div>
    <div class="front__contact">
      <p class="contact__name">Tom Waldrick</p>
      <p class="contact__role">Owner</p>
      <p class="contact__line">555-214-8830
        <svg class="contact__icon" viewBox="0 0 24 24" aria-hidden="true"><path d="M6.6 10.8a15.1 15.1 0 0 0 6.6 6.6l2.2-2.2a1 1 0 0 1 1-.25 11.4 11.4 0 0 0 3.6.57 1 1 0 0 1 1 1V20a1 1 0 0 1-1 1A17 17 0 0 1 3 4a1 1 0 0 1 1-1h3.5a1 1 0 0 1 1 1c0 1.25.2 2.45.57 3.6a1 1 0 0 1-.25 1z"/></svg>
      </p>
      <p class="contact__line">Ashford Ridge, OH
        <svg class="contact__icon" viewBox="0 0 24 24" aria-hidden="true"><path d="M12 2a7 7 0 0 0-7 7c0 5.2 7 13 7 13s7-7.8 7-13a7 7 0 0 0-7-7zm0 9.5A2.5 2.5 0 1 1 12 6.5a2.5 2.5 0 0 1 0 5z"/></svg>
      </p>
    </div>
  </section>

  <section class="card card--back" aria-label="Business card back">
    <div class="back__brand">
      <span class="brand__mark"></span>
      <span class="brand__name">Birchline Septic Solutions</span>
    </div>
    <p class="back__services">Pumping<span class="services__sep">/</span>Inspections<span class="services__sep">/</span>Installs<span class="services__sep">/</span>Repairs</p>
  </section>
</main>
</body>
</html>
```